Cardiology practice business card

We need a business card for our cardiology practice "Bellmoor Cardiology". We have a new logo, attached below. We like the colours in the logo - red and charcoal. The front of the business card will need to have the doctors name, address, phone number and email. The back will need to have space to write 2 appointment dates and times.

```html
<!DOCTYPE html>
<html lang="en">
<head>
<meta charset="utf-8">
<title>Bellmoor Cardiology – Business Card</title>
<link rel="stylesheet" href="https://fonts.googleapis.com/css2?family=Montserrat:wght@400;500;600&display=swap">
<style>
  :root {
    --red: #de1f26;
    --charcoal: #58595b;
    --ink: #231f20;
    --grey-text: #6d6e71;
    --white: #ffffff;
  }
  * { margin: 0; padding: 0; box-sizing: border-box; }
  html, body {
    width: 895px; height: 1200px; overflow: hidden;
    background: var(--white);
    font-family: "Montserrat", Arial, sans-serif;
  }
  .sheet { position: relative; width: 895px; height: 1200px; }
  .abs { position: absolute; }

  .crop-mark { position: absolute; width: 30px; height: 30px; background: var(--ink); }
  .bleed-label {
    position: absolute; left: 0; width: 895px; text-align: center;
    font-size: 17px; letter-spacing: 0.3px; line-height: 30px; color: var(--ink);
  }
  .bleed-label.on-red { color: var(--white); }

  /* Front */
  .card-front { position: absolute; left: 0; top: 0; width: 895px; height: 537px; }
  .front-panel { left: 30px; top: 30px; width: 835px; height: 438px; background: var(--red); }
  .stripe { position: absolute; left: 30px; width: 835px; }
  .stripe.red { background: var(--red); }
  .stripe.grey { background: var(--charcoal); }

  .brand-name {
    position: absolute; left: 0; width: 895px; text-align: center;
    font-weight: 600; text-transform: uppercase; letter-spacing: 3px;
    font-size: 34px;
  }
  .brand-name.on-red { color: var(--white); top: 135px; }
  .brand-name.on-white { color: var(--red); left: 490px; width: 400px; top: 800px; font-size: 30px; letter-spacing: 2px; }

  .doctor { position: absolute; left: 100px; width: 302px; top: 337px; text-align: center; color: var(--white); }
  .doctor-name { font-size: 36px; font-weight: 600; letter-spacing: 0.5px; line-height: 44px; }
  .doctor-title { font-size: 23px; font-weight: 500; line-height: 28px; }

  .divider { left: 407px; top: 301px; width: 2px; height: 142px; background: var(--white); }

  .contact { color: var(--white); font-size: 21px; }
  .address { left: 439px; top: 296px; line-height: 29px; letter-spacing: 0.4px; }
  .contact-row { position: absolute; left: 439px; display: flex; align-items: center; }
  .contact-row svg { flex: none; }
  .contact-row span { position: absolute; left: 47px; white-space: nowrap; letter-spacing: 0.4px; }
  .phone-row { top: 386px; height: 26px; }
  .email-row { top: 423px; height: 20px; }

  /* Back */
  .card-back { position: absolute; left: 0; top: 664px; width: 895px; height: 536px; }
  .appointment-field {
    position: absolute; left: 84px; color: var(--grey-text);
    font-size: 25px; font-weight: 500; letter-spacing: 0.4px;
  }
</style>
</head>
<body>
<div class="sheet">

  <section class="card-front" aria-label="Card front">
    <div class="crop-mark" style="left:0;top:0"></div>
    <div class="crop-mark" style="left:865px;top:0"></div>
    <div class="crop-mark" style="left:0;top:507px"></div>
    <div class="crop-mark" style="left:865px;top:507px"></div>
    <div class="bleed-label" style="top:1px">Bleed area</div>
    <div class="bleed-label" style="top:507px">Bleed area</div>

    <div class="abs front-panel"></div>
    <div class="stripe red" style="top:475px;height:10px"></div>
    <div class="stripe grey" style="top:485px;height:6px"></div>
    <div class="stripe red" style="top:491px;height:16px"></div>

    <div class="brand-name on-red">Bellmoor Cardiology</div>

    <div class="doctor">
      <div class="doctor-name">MARCUS HALE</div>
      <div class="doctor-title">Doctors</div>
    </div>

    <div class="abs divider"></div>

    <div class="abs contact address">4120 Harbour Line 12,<br>Eastwick, ON K7M 3B9</div>

    <div class="contact contact-row phone-row">
      <svg width="26" height="26" viewBox="0 0 26 26" aria-hidden="true">
        <path d="M6.5 2.5 L10 7.5 L8 10 C9.5 13.5 12.5 16.5 16 18 L18.5 16 L23.5 19.5 L21 23.5 C12 23 3 14 2.5 5 Z" fill="var(--white)"/>
        <path d="M14 6 A6 6 0 0 1 20 12" stroke="var(--white)" stroke-width="1.8" fill="none"/>
        <path d="M14.5 1.5 A10 10 0 0 1 24.5 11.5" stroke="var(--white)" stroke-width="1.8" fill="none"/>
      </svg>
      <span>1 (800) 555 0142</span>
    </div>

    <div class="contact contact-row email-row">
      <svg width="26" height="20" viewBox="0 0 26 20" aria-hidden="true">
        <rect x="0.8" y="0.8" width="24.4" height="18.4" fill="none" stroke="var(--white)" stroke-width="1.6"/>
        <path d="M1 1 L13 11 L25 1 M1 19 L10 9 M25 19 L16 9" fill="none" stroke="var(--white)" stroke-width="1.6"/>
      </svg>
      <span>hello@bellmoorcardio.com</span>
    </div>
  </section>

  <section class="card-back" aria-label="Card back">
    <div class="abs" style="left:0;top:0;width:895px;height:30px;background:var(--red)"></div>
    <div class="abs" style="left:0;top:506px;width:895px;height:30px;background:var(--red)"></div>
    <div class="abs" style="left:0;top:30px;width:30px;height:476px;background:var(--red)"></div>
    <div class="abs" style="left:865px;top:30px;width:30px;height:476px;background:var(--red)"></div>
    <div class="crop-mark" style="left:0;top:0"></div>
    <div class="crop-mark" style="left:865px;top:0"></div>
    <div class="crop-mark" style="left:0;top:506px"></div>
    <div class="crop-mark" style="left:865px;top:506px"></div>
    <div class="bleed-label on-red" style="top:0">Bleed area</div>
    <div class="bleed-label on-red" style="top:506px">Bleed area</div>

    <div class="stripe red" style="top:468px;height:6px"></div>
    <div class="stripe grey" style="top:485px;height:6px"></div>

    <div class="brand-name on-white" style="top:136px">Bellmoor Cardiology</div>

    <div class="appointment-field" style="top:286px">Appointment dates: MM/dd/yy</div>
    <div class="appointment-field" style="top:343px">Appointment dates: MM/dd/yy</div>
    <div class="appointment-field" style="top:398px">Time:</div>
  </section>

</div>
</body>
</html>
```